Signage for a foam car wash facility

We need signages done for a foam car wash.
We use only premium, environment-friendly, biodegradable foam wash and cleaning products.
We are in a commercial center (mall) situated in an upscale part of town and need our signage to reflect that.
We need signages for directions (two or three smaller ones), one showing that we are here, and at the actual car wash.
We will provide our logo, the texts, some pictures of the actual location the dimensions of the signages.
We need the signages to be informative, clean, crisp, modern with the use of icons if possible and some colour so that we get the attention of clients passing -by without being too flashy.
Directions to the car wash should look like a petal of a flower directing towards the car wash

Target Market(s)

Upscale market with a school and a gym next to it. Mom and dad's dropping their children at school, offices nearby.

Industry/Entity Type

Car Wash

Requirements
Nice to have
• icons, some colors,Directions to the car wash should look like a petal of a flower directing towards the car wash

```html
<!DOCTYPE html>
<html lang="en">
<head>
<meta charset="utf-8">
<title>Verdanta Car Wash Signage Set</title>
<link href="https://fonts.googleapis.com/css2?family=Montserrat:wght@500;600;700&display=swap" rel="stylesheet">
<style>
  :root {
    --teal: #73c39f;
    --lime: #bac93a;
    --paper: #ffffff;
  }
  * { box-sizing: border-box; margin: 0; padding: 0; }
  html, body { width: 1200px; height: 1200px; overflow: hidden; background: var(--paper); }
  body { position: relative; font-family: "Montserrat", Arial, sans-serif; }

  .spec-label {
    position: absolute;
    color: var(--teal);
    font-weight: 600;
    font-size: 19px;
    letter-spacing: 2.4px;
    line-height: 1;
    white-space: nowrap;
  }

  .frame { position: absolute; border: 6px solid var(--teal); background: var(--paper); }

  /* Main sign */
  .main-sign { left: 15px; top: 15px; width: 1170px; height: 570px; border-width: 28px; border-radius: 53px; }
  .main-sign .spec-label { left: 28px; top: 30px; }
  .main-sign .brand-dot {
    position: absolute; left: 435px; top: 56px; width: 270px; height: 270px;
    border-radius: 50%; background: var(--lime);
  }
  .main-sign .brand-name {
    position: absolute; left: 0; right: 0; top: 360px; text-align: center;
    color: var(--lime); font-weight: 700; font-size: 104px; letter-spacing: 4px; line-height: 1;
    white-space: nowrap;
  }

  /* Parking signs */
  .parking { left: 15px; width: 728px; height: 90px; border-radius: 30px; }
  .parking-1 { top: 656px; }
  .parking-2 { top: 770px; }
  .parking .brand-dot {
    position: absolute; left: 32px; top: 22px; width: 34px; height: 34px;
    border-radius: 50%; background: var(--lime);
  }
  .parking .word {
    position: absolute; left: 122px; top: 8px; width: 478px; height: 66px;
    display: flex; justify-content: space-between; align-items: center;
    color: var(--teal); font-weight: 600; font-size: 72px; line-height: 1;
  }
  .parking .bay-number {
    position: absolute; left: 643px; top: 13px; width: 52px; height: 52px; border-radius: 50%;
    background: var(--lime); color: var(--paper); font-weight: 700; font-size: 36px;
    line-height: 52px; text-align: center;
  }

  /* Arrow signs */
  .arrow-sign { left: 992px; width: 190px; height: 91px; border-width: 5px; border-radius: 8px; }
  .arrow-right { top: 656px; }
  .arrow-left { top: 771px; }
  .arrow-sign .brand-name {
    position: absolute; top: 30px; color: var(--lime); font-weight: 700; font-size: 15px; letter-spacing: 0.5px;
    white-space: nowrap;
  }
  .arrow-right .brand-name { left: 8px; }
  .arrow-left .brand-name { right: 8px; }
  .arrow-sign svg { position: absolute; top: 14px; width: 64px; height: 58px; }
  .arrow-right svg { right: 8px; }
  .arrow-left svg { left: 8px; }

  /* Wash bay sign */
  .wash-bay { left: 15px; top: 938px; width: 971px; height: 233px; border-width: 10px; border-radius: 22px; }
  .wash-bay .brand-dot {
    position: absolute; left: 137px; top: 22px; width: 96px; height: 96px;
    border-radius: 50%; background: var(--lime);
  }
  .wash-bay .brand-name {
    position: absolute; left: 60px; width: 250px; top: 140px; text-align: center;
    color: var(--lime); font-weight: 700; font-size: 38px; letter-spacing: 1px; line-height: 1;
    white-space: nowrap;
  }
  .wash-bay .word {
    position: absolute; left: 352px; top: 56px;
    color: var(--teal); font-weight: 700; font-size: 96px; letter-spacing: 0; line-height: 1;
    white-space: nowrap;
  }
</style>
</head>
<body>

  <section class="frame main-sign">
    <p class="spec-label">244x120cm MAIN SIGN</p>
    <div class="brand-dot"></div>
    <p class="brand-name">VERDANTA</p>
  </section>

  <p class="spec-label" style="left:17px; top:625px;">150x20cm PARKING SIGNS FOR DRY CLEAN AREA</p>
  <p class="spec-label" style="right:17px; top:625px;">40x20cm ARROW SIGNS</p>

  <section class="frame parking parking-1">
    <div class="brand-dot"></div>
    <p class="word" aria-label="PARKING"><span>P</span><span>A</span><span>R</span><span>K</span><span>I</span><span>N</span><span>G</span></p>
    <span class="bay-number">1</span>
  </section>

  <section class="frame parking parking-2">
    <div class="brand-dot"></div>
    <p class="word" aria-label="PARKING"><span>P</span><span>A</span><span>R</span><span>K</span><span>I</span><span>N</span><span>G</span></p>
    <span class="bay-number">2</span>
  </section>

  <section class="frame arrow-sign arrow-right">
    <p class="brand-name">VERDANTA</p>
    <svg viewBox="0 0 64 58" aria-hidden="true">
      <path d="M6 4 C4 1 8 0 10 0 C28 4 44 12 60 23 C64 26 64 31 60 34 C44 45 28 53 10 57 C7 58 4 57 4 54 C2 38 2 20 6 4 Z" fill="var(--teal)"/>
    </svg>
  </section>

  <section class="frame arrow-sign arrow-left">
    <svg viewBox="0 0 64 58" aria-hidden="true">
      <path d="M58 4 C60 1 56 0 54 0 C36 4 20 12 4 23 C0 26 0 31 4 34 C20 45 36 53 54 57 C57 58 60 57 60 54 C62 38 62 20 58 4 Z" fill="var(--teal)"/>
    </svg>
    <p class="brand-name">VERDANTA</p>
  </section>

  <p class="spec-label" style="left:19px; top:907px;">200x50cm WASH BAY SIGN</p>

  <section class="frame wash-bay">
    <div class="brand-dot"></div>
    <p class="brand-name">VERDANTA</p>
    <p class="word">WASH BAY</p>
  </section>

</body>
</html>
```